Varn Medical needs bold attention catching website for healthcare professionals(target)

I need a hero page as well as a products and about page for a website of mine. I specialize in orthopedic instruments . Specifically bone drills and saws. This whole company was founded to bring superb quality highly discounted medical instruments. Specifically bone drills, bone saws, k-wires and pins. Two main points should be cost savings and superior quality.

Target Market(s)

healthcare professionals Surgeons and hospital material managers

Number of Pages Required

3 page

Font styles to use
Serif

Colors

Designer to choose colors to be used in the design.

Requirements
Must have
• colors should match logo design

```html
<!DOCTYPE html>
<html lang="en">
<head>
<meta charset="utf-8">
<title>About – Varn Medical</title>
<link href="https://fonts.googleapis.com/css2?family=PT+Serif:wght@400;700&family=Open+Sans:wght@400;600&display=swap" rel="stylesheet">
<style>
:root{
  --orange:#f7901e;
  --ink:#1f1f1f;
  --body:#6b6b6b;
  --pale:#f6f8fc;
  --footer:#2b2b2b;
  --white:#ffffff;
  --line:#d9d9d9;
}
*{margin:0;padding:0;box-sizing:border-box}
html,body{width:835px;height:1200px;overflow:hidden;background:var(--white)}
body{position:relative;font-family:'Open Sans',sans-serif;color:var(--ink)}
.serif{font-family:'PT Serif',serif}
a{color:inherit;text-decoration:none}

/* header */
.site-header{position:absolute;left:0;top:0;width:835px;height:78px;background:var(--white)}
.brand{position:absolute;left:121px;top:26px;display:flex;align-items:center;gap:6px;font-family:'PT Serif',serif;font-size:17px;color:var(--orange);letter-spacing:.3px}
.brand-dot{width:10px;height:10px;border-radius:50%;background:var(--orange)}
.main-nav{position:absolute;left:300px;top:32px;display:flex;gap:16px;font-family:'PT Serif',serif;font-size:8.4px;color:var(--ink)}
.main-nav .active{color:var(--orange)}
.main-nav .caret{font-size:6px;margin-left:2px}
.search{position:absolute;left:601px;top:27px;width:99px;height:24px;border:1px solid #9a9a9a;border-radius:4px;font-size:7.5px;color:#888;padding:7px 0 0 8px}
.search svg{position:absolute;right:8px;top:8px}

/* hero */
.hero{position:absolute;left:0;top:78px;width:835px;height:217px;background:linear-gradient(100deg,#7f8893 0%,#a9adb1 35%,#b9bab9 60%,#c9c9c8 100%);text-align:center;color:var(--white)}
.hero-eyebrow{position:absolute;left:0;right:0;top:63px;font-family:'PT Serif',serif;font-size:21px;color:var(--orange)}
.hero-title{position:absolute;left:0;right:0;top:94px;font-family:'PT Serif',serif;font-weight:700;font-size:27px}
.hero-sub{position:absolute;left:0;right:0;top:138px;font-size:8.4px}

/* about */
.about{position:absolute;left:0;top:295px;width:835px;height:241px}
.about-text{position:absolute;left:121px;top:58px;width:336px;font-size:7.3px;line-height:15.7px;color:var(--body)}
.about-text em{font-style:normal;color:var(--orange)}
.about-mark{position:absolute;left:503px;top:100px;display:flex;align-items:center;gap:10px;font-family:'PT Serif',serif;font-size:30px;color:var(--orange)}
.about-mark .brand-dot{width:18px;height:18px}

/* why */
.why{position:absolute;left:0;top:536px;width:835px;height:285px;background:var(--pale);text-align:center}
.why h2{position:absolute;left:0;right:0;top:57px;font-family:'PT Serif',serif;font-weight:400;font-size:23px;color:var(--ink)}
.why h2 .accent{color:var(--orange);font-weight:700}
.why h2 strong{font-weight:700}
.why-intro{position:absolute;left:180px;width:475px;top:94px;font-size:8.4px;line-height:15px;color:var(--body)}
.feature{position:absolute;top:154px;width:140px;text-align:center;font-family:'PT Serif',serif;font-size:9.4px;line-height:14.6px;color:var(--ink)}
.feature svg{display:block;margin:0 auto 8px}

/* cta band */
.assist{position:absolute;left:0;top:821px;width:835px;height:141px;background:var(--orange);color:var(--white);text-align:center}
.assist h3{position:absolute;left:0;right:0;top:50px;font-family:'PT Serif',serif;font-weight:400;font-size:15px}
.assist-call{position:absolute;left:0;right:0;top:76px;font-size:8.4px}
.assist-call a{font-family:'PT Serif',serif;font-weight:700;font-size:12px;text-decoration:underline}

/* footer */
.site-footer{position:absolute;left:0;top:962px;width:835px;height:238px;background:var(--footer);color:var(--white)}
.footer-links{position:absolute;left:0;right:0;top:38px;display:flex;justify-content:center;font-family:'PT Serif',serif;font-size:10px}
.footer-links span{padding:0 15px;border-left:1px solid var(--orange)}
.footer-links span:first-child{border-left:none}
.footer-col{position:absolute;top:87px}
.footer-col h4{font-family:'PT Serif',serif;font-weight:400;font-size:14.6px;color:var(--orange);margin-bottom:12px}
.cert-list{list-style:none;font-size:7.3px;line-height:17.8px}
.contact-list{list-style:none;font-size:7.3px;line-height:22px}
.contact-list b{color:var(--orange);font-weight:600}
.contact-list svg{vertical-align:-1px;margin-right:4px}
.news-input{width:134px;height:25px;background:var(--white);border-radius:3px;font-size:7px;color:#9a9a9a;padding:8px 0 0 13px}
.news-btn{margin-top:8px;width:67px;height:24px;background:var(--orange);border-radius:3px;font-family:'PT Serif',serif;font-size:7.5px;text-align:center;padding-top:7px}
.copyright{position:absolute;left:121px;top:214px;font-size:6.8px}
.legal{position:absolute;right:135px;top:214px;font-size:6.8px}
.legal i{font-style:normal;margin:0 6px}
</style>
</head>
<body>

<header class="site-header">
  <div class="brand"><span class="brand-dot"></span>Varn Medical</div>
  <nav class="main-nav">
    <a>Home</a>
    <a class="active">About Us</a>
    <a>Products<span class="caret">&#8964;</span></a>
    <a>Pricing<span class="caret">&#8964;</span></a>
    <a>Contact Us</a>
  </nav>
  <div class="search">Search
    <svg width="7" height="7" viewBox="0 0 10 10"><circle cx="4" cy="4" r="3" fill="none" stroke="#666" stroke-width="1.4"/><line x1="6.2" y1="6.2" x2="9" y2="9" stroke="#666" stroke-width="1.4"/></svg>
  </div>
</header>

<section class="hero" role="img" aria-label="Photo of a doctor's hand writing on a clipboard">
  <div class="hero-eyebrow">About</div>
  <div class="hero-title">VARN MEDICAL</div>
  <p class="hero-sub">Lorem ipsum dolor sit amet, consectetur adipiscing elit, sed do eiusmod tempor incididunt</p>
</section>

<section class="about">
  <p class="about-text">Hospitals are increasingly seeking ways to cut cost while continuing to deliver high quality medical care. <em>Varn Medical</em> was created to offer hospitals and physicians high-quality products at a significantly lower cost. <em>Varn Medical</em> focus is on the orthopedic disposable market by providing quality generic products that are utilized to replace many legacy products that have low physician preference and are subject to 5%-10% annual unsustainable price increases. <em>Varn Medical</em> works directly with hospital administrators, department heads, and physicians to reduce cost that is incurred by a traditional medical device sales force. Utilizing this model, <em>Varn Medical</em> has been able to pass along cost savings of up to 50%-60%to its customers.</p>
  <div class="about-mark"><span class="brand-dot"></span>Varn Medical</div>
</section>

<section class="why">
  <h2>Why choose <span class="accent">VARN</span> <strong>MEDICAL ?</strong></h2>
  <p class="why-intro">Lorem ipsum dolor sit amet, consectetur adipiscing elit, sed do eiusmod tempor incididunt ut labore et dolore magna aliqua. Ut enim ad minim quisexercitation ullamco laboris nisi ut aliquip ex ea commodo consequat.</p>

  <div class="feature" style="left:117px">
    <svg width="32" height="30" viewBox="0 0 32 30" fill="none" stroke="#f7901e" stroke-width="1.3"><path d="M8 10h16l5 5-13 14L3 15z"/><path d="M3 15h26M12 10l-3 5 7 14 7-14-3-5"/><path d="M16 1v5M8 3l2 3M24 3l-2 3"/></svg>
    Superior Quality &amp; Competitive Pricing.
  </div>
  <div class="feature" style="left:265px">
    <svg width="26" height="30" viewBox="0 0 26 30" fill="none" stroke="#f7901e" stroke-width="1.3"><rect x="2" y="14" width="6" height="13"/><path d="M8 15l5-6V5h2l1 3v5h7l-1 14H8"/><path d="M14 1v2M19 3l-1 2M10 3l1 2"/></svg>
    Two Decades Of Experience
  </div>
  <div class="feature" style="left:416px">
    <svg width="30" height="24" viewBox="0 0 30 24" fill="none" stroke="#f7901e" stroke-width="1.3"><path d="M2 3h16v14H2z"/><path d="M18 8h6l4 5v4H18"/><circle cx="8" cy="19" r="3" fill="#f6f8fc"/><circle cx="22" cy="19" r="3" fill="#f6f8fc"/></svg>
    We export to everywhere in 110 countries
  </div>
  <div class="feature" style="left:563px">
    <svg width="26" height="26" viewBox="0 0 26 26" fill="none" stroke="#f7901e" stroke-width="1.3"><circle cx="13" cy="13" r="11.5"/><path d="M10.5 7h5v3.5H19v5h-3.5V19h-5v-3.5H7v-5h3.5z"/></svg>
    Created more than 100 Orthopedic Tools
  </div>
</section>

<section class="assist">
  <h3>Need any type of assistance related to our orthopedic instruments ?</h3>
  <p class="assist-call">
    <svg width="7" height="7" viewBox="0 0 10 10"><path d="M2 0l2 2.5-1.2 1.3a6 6 0 0 0 3.4 3.4L7.5 6 10 8l-1.5 2C4 10 0 6 0 1.5z" fill="#fff"/></svg>
    Call Us at <a>+123 456 70042</a>
  </p>
</section>

<footer class="site-footer">
  <nav class="footer-links">
    <span>Our Products</span><span>News &amp; Events</span><span>Become a Distributor</span><span>FAQ’s</span><span>Vendor Registartion</span>
  </nav>

  <div class="footer-col" style="left:121px">
    <h4>Certificates</h4>
    <ul class="cert-list">
      <li>ISO : 9001-2015</li><li>ISO 13485:2016</li><li>Quality Policy</li><li>WHO: GMP Compliance</li>
    </ul>
  </div>

  <div class="footer-col" style="left:269px">
    <h4>Get In Touch</h4>
    <ul class="contact-list">
      <li><svg width="7" height="7" viewBox="0 0 10 10"><path d="M5 0l5 5H8.5v5H6V7H4v3H1.5V5H0z" fill="#f7901e"/></svg><b>Address:</b> 123 Your Street, Your City, United States of America (12345)</li>
      <li><svg width="7" height="7" viewBox="0 0 10 10"><path d="M2 0l2 2.5-1.2 1.3a6 6 0 0 0 3.4 3.4L7.5 6 10 8l-1.5 2C4 10 0 6 0 1.5z" fill="#f7901e"/></svg><b>Telephone:</b> +12-34-56700420 (100 lines)</li>
      <li><svg width="7" height="6" viewBox="0 0 10 8"><rect x=".6" y=".6" width="8.8" height="6.8" fill="none" stroke="#f7901e" stroke-width="1.2"/><path d="M.6.8L5 4.5 9.4.8" fill="none" stroke="#f7901e" stroke-width="1.2"/></svg><b>Email:</b> info@varnmedical.com</li>
    </ul>
  </div>

  <div class="footer-col" style="left:566px">
    <h4>Newsletter</h4>
    <div class="news-input">Enter email here...</div>
    <div class="news-btn">Subscribe</div>
  </div>

  <p class="copyright">Copyright © 2019 varnmedical.com. All rights reserved.</p>
  <p class="legal">Disclaimer<i>|</i>Privacy Policy</p>
</footer>

</body>
</html>
```